Bramblewood Counselling Group Pty Ltd

clinical psychologist in private practice needs professional stationery package: business cards, complimentary slips, envelopes, range of business letterheads, and logo (photo of lighthouse).

I work with children, adolescents, adults and older population with a range of mental health concerns, adjustment to life transitions and learning difficulties. Majority of my correspondence is with medical practitioners writing reports. I would a clean crisp professional presentation (white background, navy blue text but open to ideas). Thought about having lighthouse as watermark on envelopes. My professional organisation (GTC) logo needs to be on business cards and templates (manual gives guidelines),. The photo of lighthouse is to be included in logo.
There needs to be three letterheads. 1.Is Company only Detail "bramblewood Counselling Group Pty Ltd". 2. Include Company detail and Moira Fensham Clinical Psychologist information at KVRT. 3. Include Company detail and Moira Fensham Clinical Psychologist information at Orchardvale Medical Centre

Target Market(s)

Doctors

Industry/Entity Type

Business

Colors
0355a3
3176b5
0592cd
33a6d7

Requirements
Must have
• Picture of the lighthouse
• GTC logo
• Business name

```html
<!DOCTYPE html>
<html lang="en">
<head>
<meta charset="utf-8">
<title>Bramblewood Counselling Group – Stationery</title>
<link rel="stylesheet" href="https://fonts.googleapis.com/css2?family=Ubuntu:wght@400;500&family=Open+Sans:ital,wght@0,400;0,600;0,700;1,600&display=swap">
<style>
  :root {
    --navy: #0355a3;
    --mid-blue: #3176b5;
    --sky: #0592cd;
    --light-blue: #33a6d7;
    --rule-blue: #8fc6e6;
    --canvas: #f1f2f4;
    --paper: #ffffff;
    --ink-grey: #3a3a3a;
  }
  * { box-sizing: border-box; margin: 0; padding: 0; }
  html, body { width: 1200px; height: 1126px; overflow: hidden; }
  body { background: var(--canvas); position: relative; font-family: "Open Sans", Arial, sans-serif; }

  .sheet, .card { position: absolute; background: var(--paper); box-shadow: 2px 3px 6px rgba(0,0,0,.28); overflow: hidden; }

  /* Brand lockup: name with one plain circle */
  .brand { position: absolute; display: flex; align-items: center; }
  .brand-dot { display: block; border-radius: 50%; background: var(--mid-blue); flex: none; }
  .brand-name { font-family: "Ubuntu", Arial, sans-serif; font-weight: 500; color: var(--navy); line-height: 1.05; white-space: nowrap; }

  /* Letterhead */
  .letterhead { left: 47px; top: 58px; width: 720px; height: 1019px; }
  .letterhead .brand { left: 41px; top: 38px; }
  .letterhead .brand-dot { width: 68px; height: 68px; }
  .letterhead .brand-name { font-size: 18px; margin-left: 13px; }

  .contact-block { position: absolute; left: 569px; top: 34px; border-left: 1.5px solid var(--light-blue); padding: 4px 0 2px 10px; color: var(--navy); font-weight: 700; font-size: 10.5px; line-height: 13px; }

  .society-mark { position: absolute; display: flex; align-items: center; color: var(--ink-grey); font-weight: 600; }
  .society-mark .dot { border-radius: 50%; background: var(--ink-grey); flex: none; }
  .letterhead .society-mark { left: 569px; top: 940px; font-size: 22px; }
  .letterhead .society-mark .dot { width: 30px; height: 30px; margin-right: 8px; }

  /* Business cards */
  .card { left: 843px; width: 293px; height: 190px; }
  .card-appointment { top: 277px; }
  .card-profile { top: 509px; }

  .card-panel { position: absolute; left: 0; top: 0; width: 135px; background: var(--navy); color: #fff; }
  .card-appointment .card-panel { height: 190px; }
  .card-profile .card-panel { height: 149px; }
  .name-band { position: absolute; left: 0; top: 17px; width: 135px; background: var(--mid-blue); padding: 9px 0 0 14px; }
  .card-appointment .name-band { height: 59px; }
  .card-profile .name-band { height: 62px; padding-top: 8px; }
  .person-name { font-weight: 700; font-size: 12.5px; line-height: 15px; }
  .credentials { font-size: 6px; line-height: 8px; margin-top: 3px; font-weight: 600; }
  .role { font-weight: 700; font-size: 7.5px; line-height: 10px; margin-top: 3px; }
  .card-appointment .role { margin-top: 2px; }

  .panel-details { position: absolute; left: 14px; font-size: 7.5px; line-height: 9.5px; }
  .panel-details p + p { margin-top: 7px; }
  .card-appointment .panel-details { top: 86px; }
  .card-profile .panel-details { top: 84px; }
  .panel-note { font-style: italic; font-weight: 600; font-size: 6.6px; white-space: nowrap; }
  .strong { font-weight: 700; }

  .appointment-form { position: absolute; left: 145px; top: 14px; width: 133px; color: var(--sky); font-weight: 700; font-size: 7.5px; }
  .appointment-title { text-align: center; letter-spacing: .6px; margin-bottom: 12px; }
  .form-label { line-height: 10px; }
  .form-line { height: 18px; border-bottom: 1px solid var(--rule-blue); }
  .form-line.first { height: 2px; }
  .form-label.time { margin-top: 2px; }

  .card-profile .brand { left: 147px; top: 24px; }
  .card-profile .brand-dot { width: 42px; height: 42px; }
  .card-profile .brand-name { font-size: 10px; margin-left: 7px; }
  .card-profile .society-mark { left: 212px; top: 115px; font-size: 13px; }
  .card-profile .society-mark .dot { width: 17px; height: 17px; margin-right: 5px; }

  .card-footer { position: absolute; left: 0; top: 149px; width: 293px; height: 41px; background: var(--light-blue); color: #fff; text-align: center; padding-top: 6px; }
  .services { font-size: 6.3px; font-weight: 700; letter-spacing: .2px; line-height: 10px; }
  .web { font-size: 8px; font-weight: 700; line-height: 13px; }
</style>
</head>
<body>

<section class="sheet letterhead" aria-label="Letterhead">
  <div class="brand">
    <span class="brand-dot" aria-hidden="true"></span>
    <p class="brand-name">Bramblewood<br>Counselling Group<br>Pty Ltd</p>
  </div>
  <div class="contact-block">
    <p>TEL: 07 5120 3381</p>
    <p>FAX: 07 5120 3390</p>
    <p>admin@kvrt.com.au</p>
    <p>www.kvrt.com.au</p>
    <p>ABN: 48 217 503 116</p>
  </div>
  <div class="society-mark"><span class="dot"></span>GTC</div>
</section>

<section class="card card-appointment" aria-label="Business card, appointment side">
  <div class="card-panel">
    <div class="name-band">
      <p class="person-name">Moira Fensham</p>
      <p class="role">Clinical Psychologist</p>
    </div>
    <div class="panel-details">
      <p>Ph: (07) 5120 3381</p>
      <p>Suite 3, 12 Calloway St<br>Ashgrove, Q 4060<br>admin@kvrt.com.au</p>
      <p><span class="panel-note">If you are unable to attend,<br>please inform us as soon as possible.</span><br><span class="strong">Ph: (07) 5120 3381</span></p>
    </div>
  </div>
  <div class="appointment-form">
    <p class="appointment-title">APPOINTMENT</p>
    <p class="form-label">DAY/DATE</p>
    <div class="form-line first"></div>
    <div class="form-line"></div>
    <div class="form-line"></div>
    <div class="form-line"></div>
    <p class="form-label time">TIME</p>
    <div class="form-line first"></div>
    <div class="form-line"></div>
    <div class="form-line"></div>
  </div>
</section>

<section class="card card-profile" aria-label="Business card, profile side">
  <div class="card-panel">
    <div class="name-band">
      <p class="person-name">Moira Fensham</p>
      <p class="credentials">BSc (Psych) BSc (Hons) GradDipEd<br>MPsych (Clinical) MGTC</p>
      <p class="role">Clinical Psychologist</p>
    </div>
    <div class="panel-details">
      <p>Ph: (07) 5120 3381</p>
      <p>Suite 3, 12 Calloway St<br>Ashgrove, Q 4060<br>Fax: (07) 5120 3390<br>admin@kvrt.com.au</p>
    </div>
  </div>
  <div class="brand">
    <span class="brand-dot" aria-hidden="true"></span>
    <p class="brand-name">Bramblewood<br>Counselling Group<br>Pty Ltd</p>
  </div>
  <div class="society-mark"><span class="dot"></span>GTC</div>
  <div class="card-footer">
    <p class="services">INDIVIDUAL &amp; GROUP THERAPY • ASSESSMENT • FOR CHILDREN, YOUTH &amp; ADULTS</p>
    <p class="web">www.callowaycounselling.com.au</p>
  </div>
</section>

</body>
</html>
```